Enterprise Application UI beautification

We have an enterprise application that is being redesigned. A screenshot from the new UX/UI is provided. The current UI design is OK but we would like it to look better. The key goals of the UI are to look like a premium product (think luxury brand) and for it to be visually very appealing/attractive. When people see the UI we want them to have a significant, positive reaction. They should "ooh" and "ahh". This is a product sold to large enterprises, not consumers. The current UI is a little plain. The colors we want to use are blue, yellow, black, white and gray. We probably don't want different colors but feel free to use any variations within or close to that color scheme that you see fit. Also feel free to modify the spacing, icons, widgets, tables, fonts, etc.

Target Market(s)

Large enterprise customers (Summit 300).

Number of Pages Required

1 page

Font styles to use
Sans Serif

Colors
3277b5

Requirements
Must have
• A premium feel.

```html
<!DOCTYPE html>
<html lang="en">
<head>
<meta charset="utf-8">
<title>Enterprise Dashboard – Dark</title>
<link href="https://fonts.googleapis.com/css2?family=Poppins:wght@400;500;600&display=swap" rel="stylesheet">
<style>
:root{
  --page:#ffffff;
  --app-bg:#1b1b22;
  --rail:#121216;
  --panel:#1d1d26;
  --card:#22222c;
  --row-alt:#1f1f2b;
  --line:#2c2c38;
  --text:#ffffff;
  --muted:#9a9aa8;
  --dim:#6f6f7c;
  --accent:#a55fdb;
  --blue:#1a6cf5;
  --chip:#4a4a56;
  --icon-tile:#5a5a63;
  --yellow:#e2a93b;
  --green:#7bc44a;
  --red:#e5484d;
}
*{box-sizing:border-box;margin:0;padding:0}
html,body{width:1200px;height:1200px;overflow:hidden;background:var(--page);font-family:"Poppins",sans-serif}
.board-label{position:absolute;left:94px;top:925px;font-size:4.5px;line-height:6px;color:#b8b8b8;font-family:"Times New Roman",serif;letter-spacing:.2px}
.board-rule{position:absolute;left:0;top:943px;width:165px;height:1px;background:#cfcfcf}
.app{position:absolute;left:88px;top:320px;width:1024px;height:560px;background:var(--app-bg);overflow:hidden;box-shadow:0 14px 30px rgba(0,0,0,.18);color:var(--text)}
.rail{position:absolute;left:0;top:0;width:55px;height:560px;background:var(--rail)}
.brand{position:absolute;left:6px;top:18px;font-size:9px;font-weight:600;color:var(--text);display:flex;align-items:center;gap:3px}
.brand i{width:6px;height:6px;border-radius:50%;background:var(--text);display:block}
.rail-icon{position:absolute;left:16px;width:23px;height:23px;border-radius:5px;background:var(--icon-tile);display:flex;align-items:center;justify-content:center}
.rail-icon.active{background:#fff}
.rail-icon.add{background:none;border:1px dashed #777}
.badge{position:absolute;right:-6px;top:-6px;width:11px;height:11px;border-radius:50%;background:var(--red);font-size:7px;line-height:11px;text-align:center;font-weight:500}
.topbar{position:absolute;left:55px;top:0;right:0;height:55px;border-bottom:1px solid var(--line)}
.user{position:absolute;right:16px;top:18px;display:flex;align-items:center;gap:6px}
.avatar{width:19px;height:19px;border-radius:50%;background:linear-gradient(135deg,#c9a7a0,#7a3b3b)}
.user-name{font-size:10px;font-weight:600;line-height:12px}
.user-role{font-size:7px;color:var(--muted)}
.caret{width:12px;height:12px;border:1px solid #bbb;border-radius:50%;margin-left:6px;display:flex;align-items:center;justify-content:center}
.sources{position:absolute;left:55px;top:55px;width:233px;height:505px;background:var(--panel)}
.h2{font-size:15px;font-weight:500}
.sources .h2{position:absolute;left:16px;top:14px}
.btn-add{position:absolute;left:165px;top:13px;width:48px;height:18px;border-radius:4px;background:var(--blue);font-size:10px;font-weight:500;display:flex;align-items:center;justify-content:center}
.search{position:absolute;left:16px;top:45px;width:198px;height:31px;border-radius:8px;background:#17171d;font-size:11px;color:#d8d8d8;display:flex;align-items:center;padding-left:12px;gap:8px}
.src{position:absolute;left:9px;width:218px;height:51px;border-radius:6px;padding:12px 12px 0}
.src.selected{background:var(--accent)}
.src-name{font-size:12px;font-weight:500;line-height:15px}
.src-type{font-size:9px;color:var(--muted);line-height:13px}
.src.selected .src-type{color:#e8d6f6}
.scroll{position:absolute;left:229px;top:95px;width:3px;height:410px;background:#e8e8e8}
.scroll-thumb{position:absolute;left:229px;top:95px;width:3px;height:83px;background:#2f7ff0}
.title{position:absolute;left:310px;top:73px;font-size:15px;font-weight:500}
.chip{position:absolute;top:74px;height:19px;border-radius:4px;background:var(--chip);font-size:10px;font-weight:500;display:flex;align-items:center;justify-content:center;gap:3px}
.sep{position:absolute;top:79px;width:1px;height:7px;background:#aaa}
.info{position:absolute;left:310px;top:106px;width:697px;height:114px;border-radius:8px;background:var(--card);font-size:9.5px}
.info span{position:absolute;line-height:12px}
.info .k{font-weight:500}
.info .v{color:#e6e6e6}
.objects-title{position:absolute;left:310px;top:241px}
.chip.add-obj{top:241px;left:422px;width:47px}
.section{position:absolute;left:310px;width:697px;border:1px solid var(--line);border-radius:8px;background:var(--app-bg)}
.sec-name{position:absolute;left:16px;font-size:10px;font-weight:500;color:#cfcfd6;display:flex;align-items:center;gap:7px}
.toggle{width:15px;height:15px;border:1px solid #bbb;border-radius:50%;display:flex;align-items:center;justify-content:center}
.dots{position:absolute;right:18px;font-size:10px;color:#ccc;letter-spacing:1px}
.thead{position:absolute;left:7px;top:32px;width:684px;height:22px;border-radius:5px;background:#2a2a34;font-size:9.5px;color:var(--dim);font-weight:500}
.thead span,.row span{position:absolute}
.thead span{top:4px}
.row{position:absolute;left:7px;width:684px;height:29px;font-size:9.5px}
.row.alt{background:var(--row-alt)}
.row .field{left:16px;top:7px}
.bar{width:1px;height:12px;background:#ddd;top:8px}
.check{width:9px;height:9px;border:1px solid #888;border-radius:2px;top:10px;left:338px}
.check.on{background:#2f7ff0;border-color:#2f7ff0}
.rules{left:395px;top:7px;display:flex;gap:9px;align-items:center;font-size:10px}
.rules b{font-weight:600;font-size:12px;line-height:12px}
.sens{left:513px;top:8px;display:flex;gap:9px}
.acts{left:611px;top:7px;display:flex;gap:11px}
</style>
</head>
<body>
<div class="board-label">ENTERPRISE DASH BOARD<br>DARK VERSION // V01</div>
<div class="board-rule"></div>

<main class="app">
  <nav class="rail">
    <div class="brand"><i></i>Vantix</div>
    <div class="rail-icon" style="top:90px"><svg width="13" height="11" viewBox="0 0 13 11"><circle cx="6.5" cy="3" r="2" fill="none" stroke="#e2a93b" stroke-width="1.2"/><circle cx="2.5" cy="4" r="1.5" fill="none" stroke="#e2a93b"/><circle cx="10.5" cy="4" r="1.5" fill="none" stroke="#e2a93b"/><path d="M2 10c0-3 9-3 9 0" fill="none" stroke="#e2a93b" stroke-width="1.2"/></svg></div>
    <div class="rail-icon" style="top:144px"><svg width="14" height="10" viewBox="0 0 14 10"><path d="M3 9a3 3 0 0 1 0-6 4 4 0 0 1 7.5 0A3 3 0 0 1 11 9z" fill="#e2a93b"/></svg></div>
    <div class="rail-icon active" style="top:198px"><svg width="14" height="13" viewBox="0 0 14 13"><path d="M7 1l6 3-6 3-6-3z M1 6.5l6 3 6-3 M1 9l6 3 6-3" fill="none" stroke="#e2a93b" stroke-width="1.3"/></svg></div>
    <div class="rail-icon" style="top:253px"><svg width="10" height="13" viewBox="0 0 10 13"><rect x="1" y="2" width="8" height="10" rx="1" fill="none" stroke="#e2a93b" stroke-width="1.2"/><path d="M3 6h4M3 8.5h4" stroke="#e2a93b"/></svg></div>
    <div class="rail-icon" style="top:307px"><svg width="12" height="12" viewBox="0 0 12 12"><rect x="1" y="2" width="10" height="9" rx="1" fill="none" stroke="#e2a93b" stroke-width="1.2"/><path d="M1 5h10M3 7h1M5.5 7h1M8 7h1M3 9h1M5.5 9h1" stroke="#e2a93b"/></svg><div class="badge">3</div></div>
    <div class="rail-icon" style="top:362px"><svg width="12" height="12" viewBox="0 0 12 12"><circle cx="3" cy="3" r="1.7" fill="none" stroke="#e2a93b"/><circle cx="9" cy="9" r="1.7" fill="none" stroke="#e2a93b"/><path d="M3 5v4h4M9 7V3H5" fill="none" stroke="#e2a93b"/></svg></div>
    <div class="rail-icon add" style="top:416px"><svg width="10" height="10" viewBox="0 0 10 10"><path d="M5 1v8M1 5h8" stroke="#fff" stroke-width="1.4"/></svg></div>
  </nav>

  <header class="topbar">
    <div class="user">
      <div class="avatar" role="img" aria-label="User portrait"></div>
      <div><div class="user-name">Nora Vale</div><div class="user-role">Dev Administrator</div></div>
      <div class="caret"><svg width="5" height="3" viewBox="0 0 5 3"><path d="M.5.5l2 2 2-2" fill="none" stroke="#ccc" stroke-width=".8"/></svg></div>
    </div>
  </header>

  <aside class="sources">
    <div class="h2">Data Sources</div>
    <div class="btn-add">+ Add</div>
    <div class="search"><svg width="8" height="8" viewBox="0 0 8 8"><circle cx="3.3" cy="3.3" r="2.5" fill="none" stroke="#aaa"/><path d="M5.2 5.2L7.5 7.5" stroke="#aaa"/></svg>Search...</div>
    <div class="src selected" style="top:95px"><div class="src-name">Cloudforge - Sandbox</div><div class="src-type">Cloudforge.io</div></div>
    <div class="src" style="top:146px"><div class="src-name">TableBase Test 1 (administrator)</div><div class="src-type">TableBase SQL</div></div>
    <div class="src" style="top:197px"><div class="src-name">TableBase Test 2 (administrator)</div><div class="src-type">Cloudforge.io</div></div>
    <div class="src" style="top:248px"><div class="src-name">Sadga</div><div class="src-type">Cloudforge.io</div></div>
    <div class="src" style="top:300px"><div class="src-name">Cloudforge Test 1 (masterd ev)</div><div class="src-type">TableBase SQL</div></div>
    <div class="src" style="top:351px"><div class="src-name">CFDC - Field Entry Test</div><div class="src-type">Cloudforge.io</div></div>
    <div class="src" style="top:402px"><div class="src-name">CFDC 44</div><div class="src-type">Cloudforge.io</div></div>
    <div class="src" style="top:453px"><div class="src-name">CFDC 66</div><div class="src-type">Cloudforge.io</div></div>
    <div class="scroll"></div><div class="scroll-thumb"></div>
  </aside>

  <section class="detail">
    <div class="title">Cloudforge - Sandbox</div>
    <div class="chip" style="left:486px;width:47px">✎ Edit</div>
    <div class="sep" style="left:543px"></div>
    <div class="chip" style="left:553px;width:54px">⧉ Clone</div>
    <div class="sep" style="left:617px"></div>
    <div class="chip" style="left:627px;width:57px">🗑︎ Delete</div>
    <div class="chip" style="left:902px;width:105px">◔ Test Connection</div>

    <div class="info">
      <span class="k" style="left:16px;top:16px">Data source name</span><span class="v" style="left:141px;top:17px">Cloudforge-Sandbox</span>
      <span class="k" style="left:16px;top:34px">Data Source Type</span><span class="v" style="left:141px;top:35px">Application</span>
      <span class="k" style="left:16px;top:52px">Status</span><span class="v" style="left:141px;top:52px">Active</span>
      <span class="k" style="left:16px;top:70px">Created By</span><span class="v" style="left:141px;top:70px">harlow.test</span>
      <span class="k" style="left:16px;top:88px">Last updated By</span><span class="v" style="left:141px;top:88px">harlow.test</span>
      <span class="k" style="left:326px;top:17px">Username</span><span class="v" style="left:444px;top:17px">masterdev@dev.northdata.net</span>
      <span class="k" style="left:326px;top:35px">Security Token</span><span class="v" style="left:444px;top:35px">tadkaji4234ifndkn3</span>
      <span class="k" style="left:326px;top:52px">Environment Type</span><span class="v" style="left:444px;top:52px">Production</span>
      <span class="k" style="left:326px;top:70px">Connected App</span><span class="v" style="left:444px;top:70px">No</span>
    </div>

    <div class="h2 objects-title">Data Objects</div>
    <div class="chip add-obj">+ Add</div>

    <div class="section" style="top:268px;height:172px">
      <div class="sec-name" style="top:7px">Account <span class="toggle"><svg width="5" height="3" viewBox="0 0 5 3"><path d="M.5 2.5l2-2 2 2" fill="none" stroke="#ccc" stroke-width=".8"/></svg></span></div>
      <div class="dots" style="top:6px">···</div>
      <div class="thead">
        <span style="left:9px">Field Name</span><span style="left:157px">Data Type</span><span style="left:313px">Primary Key</span><span style="left:387px">Rule Types</span><span style="left:505px">Sensitive Data</span><span style="left:601px">Actions</span>
      </div>
      <div class="row" style="top:56px">
        <span class="field">Account description</span><span class="bar" style="left:150px"></span><span class="bar" style="left:307px"></span>
        <span class="check on"></span><span class="bar" style="left:380px"></span>
        <span class="rules"><b style="color:#777">a</b>⌕ ▣ ⑂ ⌖ ▸</span><span class="bar" style="left:499px"></span>
        <span class="sens">▤ ▬ ● ▣</span><span class="bar" style="left:595px"></span>
        <span class="acts">✎ ✕</span>
      </div>
      <div class="row alt" style="top:85px">
        <span class="field">Account Fax</span><span class="bar" style="left:150px"></span><span class="bar" style="left:307px"></span>
        <span class="check"></span><span class="bar" style="left:380px"></span>
        <span class="rules"><b>a</b>⌕ <span style="position:static;color:#777">▣</span> ⑂ ⌖ ▸</span><span class="bar" style="left:499px"></span>
        <span class="bar" style="left:595px"></span><span class="acts">✎ ✕</span>
      </div>
      <div class="row" style="top:114px">
        <span class="field">Address ID</span><span class="bar" style="left:150px"></span><span class="bar" style="left:307px"></span>
        <span class="check"></span><span class="bar" style="left:380px"></span>
        <span class="rules"><b style="color:#b86be0">a</b><span style="position:static;color:var(--green)">⌕</span> ▣ ⑂ ⌖ ▸</span><span class="bar" style="left:499px"></span>
        <span class="bar" style="left:595px"></span><span class="acts">✎ ✕</span>
      </div>
      <div class="row alt" style="top:143px">
        <span class="field">Account Name</span><span class="bar" style="left:150px"></span><span class="bar" style="left:307px"></span>
        <span class="check"></span><span class="bar" style="left:380px"></span>
        <span class="rules"><b>a</b>⌕ <span style="position:static;color:#777">▣</span> ⑂ ⌖ ▸</span><span class="bar" style="left:499px"></span>
        <span class="bar" style="left:595px"></span><span class="acts">✎ ✕</span>
      </div>
    </div>

    <div class="section" style="top:451px;height:29px">
      <div class="sec-name" style="top:6px">Asset <span class="toggle"><svg width="5" height="3" viewBox="0 0 5 3"><path d="M.5.5l2 2 2-2" fill="none" stroke="#ccc" stroke-width=".8"/></svg></span></div>
      <div class="dots" style="top:5px">···</div>
    </div>
    <div class="section" style="top:490px;height:29px">
      <div class="sec-name" style="top:6px">Asset Relationship <span class="toggle"><svg width="5" height="3" viewBox="0 0 5 3"><path d="M.5.5l2 2 2-2" fill="none" stroke="#ccc" stroke-width=".8"/></svg></span></div>
      <div class="dots" style="top:5px">···</div>
    </div>
    <div class="section" style="top:528px;height:29px">
      <div class="sec-name" style="top:6px">Asset Token Event <span class="toggle"><svg width="5" height="3" viewBox="0 0 5 3"><path d="M.5.5l2 2 2-2" fill="none" stroke="#ccc" stroke-width=".8"/></svg></span></div>
      <div class="dots" style="top:5px">···</div>
    </div>
  </section>
</main>
</body>
</html>
```